An anniversary gift for my girlfriend

My girlfriend and I have been dating for almost 2 years. We met online and this has afforded us the really unique opportunity to have the first words we said to each other (the whole conversation, in fact) preserved. We're moving in together in a few months and she doesn't know that I saved the conversation. I've been waiting for this to turn it into something we can hang in our new place.

The only phrase I want to use is:
"Well if you dislike people's knees then I think we'll get along famously"

It's an Nobody Leaves Before Midnight in Portland reference for the curious.

I want the poster to use the words themselves as the art; I'm thinking typography. I'd like it to match her aesthetic, she likes to wear Nora Vell and T. Brisk. Colors shouldn't be anything too "girly". Somewhere I'd like to include the date June 1, 2015. It shouldn't be a major piece of the poster though, just a way to denote the date.

It should fit (and be fully visible in) a 16x20 (inches) frame

Thanks in advance for the work!

Requirements
Must have
• Must use only the words: "Well if you dislike people's knees then I think we'll get along famously"
• I want this to be typography, so making the phrase the center of the poster and the art itself.

```html
<!DOCTYPE html>
<html lang="en">
<head>
<meta charset="utf-8">
<title>Well if you dislike people's knees</title>
<link rel="stylesheet" href="https://fonts.googleapis.com/css2?family=Abril+Fatface&family=Amatic+SC:wght@400&display=swap">
<style>
  :root {
    --poster-aqua: #7fe1d4;
    --ink-white: #ffffff;
  }
  html, body {
    margin: 0;
    padding: 0;
    width: 960px;
    height: 1200px;
    overflow: hidden;
    background: var(--poster-aqua);
  }
  .poster {
    display: block;
    width: 960px;
    height: 1200px;
    background: var(--poster-aqua);
  }
  .quote-line,
  .quote-mark {
    font-family: "Abril Fatface", "Georgia", serif;
    fill: var(--ink-white);
  }
  .date-stamp {
    font-family: "Amatic SC", "Arial Narrow", sans-serif;
    fill: var(--ink-white);
    letter-spacing: 3px;
  }
</style>
</head>
<body>
<svg class="poster" viewBox="0 0 960 1200" width="960" height="1200" xmlns="http://www.w3.org/2000/svg" role="img" aria-label="Well if you dislike people's knees then I think we'll get along famously — 06.01.2015">
  <text class="quote-mark quote-open" x="86" y="272" font-size="240">&#8220;</text>

  <text class="quote-line line-well" x="107" y="320" font-size="160" textLength="394" lengthAdjust="spacingAndGlyphs">Well</text>
  <text class="quote-line line-if" x="523" y="272" font-size="80" textLength="58" lengthAdjust="spacingAndGlyphs">if</text>
  <text class="quote-line line-you" x="523" y="320" font-size="85" textLength="176" lengthAdjust="spacingAndGlyphs">you</text>

  <text class="quote-line line-dislike" x="113" y="533" font-size="232" textLength="740" lengthAdjust="spacingAndGlyphs">dislike</text>

  <text class="quote-line line-knees" x="128" y="629" font-size="92" textLength="651" lengthAdjust="spacingAndGlyphs">people&#8217;s knees</text>

  <text class="quote-line line-then" x="165" y="734" font-size="120" textLength="304" lengthAdjust="spacingAndGlyphs">then I</text>
  <text class="quote-line line-think" x="496" y="688" font-size="46" textLength="229" lengthAdjust="spacingAndGlyphs">think we&#8217;ll</text>
  <text class="quote-line line-along" x="496" y="734" font-size="46" textLength="229" lengthAdjust="spacingAndGlyphs">get along</text>
  <text class="quote-mark quote-close" x="780" y="818" font-size="240">&#8221;</text>

  <text class="quote-line line-famously" x="91" y="848" font-size="152" textLength="763" lengthAdjust="spacingAndGlyphs">famously</text>

  <text class="date-stamp" x="480" y="1028" font-size="48" text-anchor="middle">06.01.2015</text>
</svg>
</body>
</html>
```